Vexo App

We want to have a web banner (4-5 slides) flash or whatever.
We are innovative next generation messenger with a good design, themes, snap mode, pinging and other features.
Inspired by night, by techno music, by energy, by innovations and next generation.
High tech.

The name of the app : Vexo
vexoapp.example

The banner will be used for nightlisting.example

We want the banner to be creative, and deliver the inspiration of the app.

All the assets, logos and so on can me delivered to you via email by request.

```html
<!DOCTYPE html>
<html lang="en">
<head>
<meta charset="utf-8">
<title>Vexo App – Web Banner Slides</title>
<link href="https://fonts.googleapis.com/css2?family=Montserrat:wght@700;800&display=swap" rel="stylesheet">
<style>
  :root {
    --page: #ffffff;
    --ink-dark: #000000;
    --panel-dark: #1e1e1e;
    --lime: #a9d82a;
    --lime-light: #c6ec3e;
    --text-light: #f2f2f2;
    --text-dark: #111111;
    --brand-blue: #7db8f6;
    --night-purple: #2b1f4a;
    --night-green: #3f6a2c;
    --city-blue: #1a2433;
    --city-deep: #0b1119;
  }
  * { margin: 0; padding: 0; box-sizing: border-box; }
  html, body {
    width: 1200px; height: 552px; overflow: hidden;
    background: var(--page);
    font-family: "Montserrat", Arial, sans-serif;
  }
  .slides { position: relative; width: 1200px; height: 552px; }
  .banner {
    position: absolute; left: 64px; width: 1079px; height: 137px;
    background: var(--ink-dark); overflow: hidden;
  }
  .banner--night { top: 31px; }
  .banner--launch { top: 210px; background: var(--panel-dark); }
  .banner--city { top: 391px; }

  .brand {
    position: absolute; left: 38px; top: 50%; transform: translateY(-50%);
    display: flex; align-items: center; gap: 12px; z-index: 3;
  }
  .brand__square { width: 22px; height: 22px; background: var(--brand-blue); }
  .brand__name {
    font-size: 36px; font-weight: 700; color: var(--text-light); letter-spacing: -0.5px;
  }

  .photo { position: absolute; top: 0; height: 100%; }
  .photo--club {
    left: 380px; right: 0;
    background:
      linear-gradient(90deg, var(--ink-dark) 0%, rgba(0,0,0,0) 18%),
      radial-gradient(ellipse at 45% 20%, #8a9fb0 0%, rgba(0,0,0,0) 40%),
      linear-gradient(100deg, var(--night-purple) 10%, #4a2f7a 45%, var(--night-green) 85%, #1a2a14 100%);
  }
  .photo--city {
    left: 219px; width: 684px;
    background:
      linear-gradient(90deg, var(--ink-dark) 0%, rgba(0,0,0,0) 10%, rgba(0,0,0,0) 88%, var(--ink-dark) 100%),
      linear-gradient(180deg, var(--city-blue) 0%, #26313f 45%, var(--city-deep) 100%);
  }
  .photo--phones {
    right: 14px; width: 220px; top: 8px; height: 129px;
    background: linear-gradient(180deg, #2a2a2a 0%, #0d0d0d 100%);
  }

  .headline {
    position: absolute; z-index: 2; font-weight: 800; text-transform: uppercase;
  }
  .headline--night {
    left: 253px; top: 50%; transform: translateY(-50%);
    font-size: 37px; color: var(--text-light); letter-spacing: 0.3px;
  }
  .headline--launch {
    left: 290px; width: 530px; top: 50%; transform: translateY(-50%);
    font-size: 25px; line-height: 1.35; color: var(--text-dark); text-align: center;
  }
  .headline--city {
    right: 32px; top: 50%; transform: translateY(-50%);
    font-size: 31px; color: var(--text-light);
  }
  .lime-field { position: absolute; inset: 0; z-index: 0; }
</style>
</head>
<body>
<main class="slides">

  <section class="banner banner--night">
    <div class="photo photo--club" role="img" aria-label="Photo of a crowded techno club with laser lights over the dance floor"></div>
    <div class="brand"><span class="brand__square"></span><span class="brand__name">Vexo</span></div>
    <h2 class="headline headline--night">Inspired by night!</h2>
  </section>

  <section class="banner banner--launch">
    <svg class="lime-field" width="1079" height="137" viewBox="0 0 1079 137" aria-hidden="true">
      <defs>
        <linearGradient id="limeGlow" x1="0" y1="0" x2="1" y2="0">
          <stop offset="0" stop-color="var(--lime)"/>
          <stop offset="0.5" stop-color="var(--lime-light)"/>
          <stop offset="1" stop-color="var(--lime)"/>
        </linearGradient>
      </defs>
      <polygon points="291,0 1079,0 1079,137 202,137" fill="url(#limeGlow)"/>
    </svg>
    <div class="photo photo--phones" role="img" aria-label="Two smartphones showing the Vexo contact list screen"></div>
    <div class="brand"><span class="brand__square"></span><span class="brand__name">Vexo</span></div>
    <h2 class="headline headline--launch">New groundbreaking messenger for your mobile now available!</h2>
  </section>

  <section class="banner banner--city">
    <div class="photo photo--city" role="img" aria-label="Night skyline of a city with lit office towers and people on a rooftop"></div>
    <div class="brand"><span class="brand__square"></span><span class="brand__name">Vexo</span></div>
    <h2 class="headline headline--city">Try it now !</h2>
  </section>

</main>
</body>
</html>
```